Criação de Layout para Website para alimenticio
" A Ve Brinola é uma empresa que produz doces finos para eventos (corporativos e sociais), cujo público alvo são consumidores que valorizam um produto de qualidade e diferenciado. "

```html
<!DOCTYPE html>
<html lang="pt-BR">
<head>
<meta charset="utf-8">
<title>Ve Brinola — Doces Finos</title>
<link rel="stylesheet" href="https://fonts.googleapis.com/css2?family=Open+Sans:wght@400;600;700&display=swap">
<style>
:root{
  --brown:#5a4f47;
  --brown-dark:#4a413a;
  --teal:#c5e9ec;
  --teal-strong:#9fd9dc;
  --panel:#f7f7f7;
  --text:#4e4640;
  --navy:#1e2235;
  --footer:#6f776b;
}
*{box-sizing:border-box;margin:0;padding:0}
html,body{width:1200px;height:2518px;overflow:hidden;background:#fff}
body{position:relative;font-family:"Open Sans",Arial,sans-serif;color:var(--text)}
.abs{position:absolute}
.social{top:82px;left:1005px;display:flex;gap:9px}
.social span{width:40px;height:40px;border-radius:50%;background:var(--brown-dark);display:block}
.search{top:133px;left:903px;width:287px;height:25px;background:#e6e6e6;border:1px solid #d6d6d6}
.search .btn{position:absolute;right:-1px;top:-1px;width:32px;height:25px;background:var(--brown)}
.nav{top:175px;left:10px;width:1182px;height:49px;background:var(--brown);color:#fff;font-weight:700;font-size:18px}
.nav a{position:absolute;top:0;height:49px;line-height:49px;color:#fff;text-decoration:none;padding:0 24px}
.nav .sep{border-right:1px solid #6d625a}
.nav .active{background:var(--teal);color:var(--brown-dark)}
.burger{position:absolute;left:24px;top:15px;width:28px}
.burger i{display:block;height:4px;background:#fff;margin-bottom:5px}
.brand{top:40px;left:420px;width:380px;height:290px;display:flex;align-items:center;justify-content:center;gap:14px;background:#fff;border-radius:18px}
.brand .mark{width:26px;height:26px;background:var(--teal-strong);border-radius:50%}
.brand .name{font-size:58px;font-weight:700;color:var(--brown)}
.panel{top:224px;left:10px;width:1182px;height:2021px;background:var(--panel);border:1px solid #e2e2e2;border-top:none}
.ph{position:absolute}
.hero-cap{position:absolute;left:393px;top:487px;width:788px;height:181px;background:rgba(30,24,24,.72);color:#fff;padding:10px 20px}
.hero-cap h2{font-weight:400;font-size:33px;letter-spacing:-.5px}
.hero-cap p{font-size:15px;line-height:26px;margin-top:8px;width:720px}
.hero-cap .more{display:inline-block;margin-top:6px;background:var(--teal);color:var(--brown-dark);font-size:14px;font-weight:600;padding:8px 12px}
.dots{position:absolute;right:20px;bottom:12px;display:flex;gap:9px}
.dots i{width:10px;height:10px;border:1.5px solid #fff;border-radius:50%;display:block}
.dots i.on{background:#fff}
.rule{top:750px;left:26px;width:1152px;height:1px;background:#cfcfcf}
.sec-title{position:absolute;left:38px;font-size:28px;font-weight:700;color:var(--brown)}
.sec-text{position:absolute;left:39px;font-size:20px;line-height:23px;color:var(--text)}
.arrows{position:absolute;left:1059px;display:flex;gap:9px}
.arrows span{width:43px;height:43px;border:2px solid var(--brown);border-radius:50%;display:flex;align-items:center;justify-content:center}
.label{position:absolute;left:0;bottom:0;width:100%;height:44px;background:var(--navy);color:#fff;font-size:13px;font-weight:700;text-align:center;line-height:44px}
.plus{position:absolute;left:50%;top:62px;transform:translateX(-50%);color:#fff;font-size:28px;font-weight:300}
.footer-line{top:2258px;left:0;width:1200px;height:10px;background:var(--teal-strong)}
.footer{top:2268px;left:0;width:1200px;height:250px;background:linear-gradient(180deg,#7a8175,#646a60)}
.fcol{position:absolute;top:2300px;color:#fff}
.fcol h3{font-size:31px;font-weight:700;color:var(--teal-strong);line-height:36px}
.fcol p{font-size:18px;line-height:22px}
.fbtn{display:inline-block;background:var(--teal);color:var(--brown-dark);font-size:12px;padding:3px 16px}
</style>
</head>
<body>

<div class="abs social" aria-label="Redes sociais"><span></span><span></span><span></span><span></span></div>
<div class="abs search"><div class="btn"><svg width="32" height="25"><circle cx="15" cy="11" r="4" fill="none" stroke="#fff" stroke-width="2"/><line x1="18" y1="14" x2="21" y2="17" stroke="#fff" stroke-width="2"/></svg></div></div>

<nav class="abs nav">
  <div class="burger"><i></i><i></i><i></i></div>
  <a style="left:76px" class="sep">HOME</a>
  <a style="left:195px" class="sep">QUEM SOMOS</a>
  <a style="left:882px;width:171px;text-align:center" class="active">PRODUTOS</a>
  <a style="left:1053px;width:129px;text-align:center">CONTATO</a>
</nav>

<div class="abs brand"><span class="mark"></span><span class="name">Ve Brinola</span></div>

<div class="abs panel"></div>

<div class="ph" style="left:22px;top:240px;width:360px;height:90px;background:linear-gradient(135deg,#6b3a22,#c7a27a)" role="img" aria-label="Mesa de doces com bolo de casamento"></div>
<div class="ph" style="left:22px;top:338px;width:360px;height:90px;background:linear-gradient(90deg,#6a5a55,#c96a9a)" role="img" aria-label="Doces decorados brancos e rosa"></div>
<div class="ph" style="left:22px;top:438px;width:360px;height:90px;background:linear-gradient(90deg,#e8e2dc,#e39a3e)" role="img" aria-label="Doces com physalis"></div>
<div class="ph" style="left:22px;top:538px;width:360px;height:90px;background:linear-gradient(90deg,#9a7a3a,#e8a93a)" role="img" aria-label="Copinhos de doce de maracujá"></div>
<div class="ph" style="left:22px;top:642px;width:360px;height:90px;background:linear-gradient(90deg,#cfd68a,#d94a80,#f1c0d0)" role="img" aria-label="Macarons coloridos"></div>
<div class="ph" style="left:393px;top:240px;width:788px;height:492px;background:linear-gradient(180deg,#d9a9ad,#9c2c34 45%,#6e3a3a)" role="img" aria-label="Docinhos com cerejas em bandeja"></div>
<div class="hero-cap">
  <h2>SEJA BEM VINDO !</h2>
  <p>Temos nossa linha fixa, no entanto produzimos doces personalizados para dar um toque exclusivo para o seu evento. Confira nossa linha de produtos.</p>
  <span class="more">SAIBA MAIS</span>
  <div class="dots"><i></i><i class="on"></i><i></i></div>
</div>

<div class="abs rule"></div>

<h2 class="sec-title" style="top:768px">DOCES FINOS</h2>
<p class="sec-text" style="top:807px">nossa linha fixa de doces, porém produzimos doces personalizados<br>para dar um toque único ao seu evento.</p>
<div class="arrows" style="top:848px"><span><svg width="14" height="20"><path d="M11 2 3 10l8 8" fill="none" stroke="#5a4f47" stroke-width="2.5"/></svg></span><span><svg width="14" height="20"><path d="M3 2l8 8-8 8" fill="none" stroke="#5a4f47" stroke-width="2.5"/></svg></span></div>

<div class="ph" style="left:34px;top:907px;width:265px;height:194px;background:linear-gradient(180deg,#4a3028,#2c1e1a)" role="img" aria-label="Brownie belga"><span class="plus">+</span><div class="label">BROWNIE BELGA</div></div>
<div class="ph" style="left:321px;top:907px;width:264px;height:194px;background:linear-gradient(135deg,#f0d070,#d84a88,#a8cc6a)" role="img" aria-label="Macarons coloridos"></div>
<div class="ph" style="left:611px;top:907px;width:265px;height:194px;background:radial-gradient(circle,#f3e7b4,#2a3a8a)" role="img" aria-label="Docinhos com confeitos perolados"></div>
<div class="ph" style="left:901px;top:907px;width:265px;height:194px;background:radial-gradient(circle,#f5f2ee,#8a7060)" role="img" aria-label="Doces em forma de flor branca"></div>
<div class="ph" style="left:34px;top:1128px;width:265px;height:194px;background:radial-gradient(circle,#f6b820,#8a3a10)" role="img" aria-label="Copinhos de maracujá"></div>
<div class="ph" style="left:321px;top:1128px;width:264px;height:194px;background:linear-gradient(180deg,#4a2a22,#1e1210)" role="img" aria-label="Docinhos de chocolate com flor"></div>
<div class="ph" style="left:611px;top:1128px;width:265px;height:194px;background:linear-gradient(135deg,#d8cfc4,#f4ede3,#9a8a7a)" role="img" aria-label="Conchas de chocolate branco com pérolas"></div>
<div class="ph" style="left:901px;top:1128px;width:265px;height:194px;background:linear-gradient(135deg,#f0c0c8,#c04050,#e8a0b0)" role="img" aria-label="Doces embrulhados em rosa"></div>

<h2 class="sec-title" style="top:1382px">BEM CASADOS</h2>
<div class="arrows" style="top:1410px"><span><svg width="14" height="20"><path d="M11 2 3 10l8 8" fill="none" stroke="#5a4f47" stroke-width="2.5"/></svg></span><span><svg width="14" height="20"><path d="M3 2l8 8-8 8" fill="none" stroke="#5a4f47" stroke-width="2.5"/></svg></span></div>

<div class="ph" style="left:34px;top:1468px;width:265px;height:194px;background:linear-gradient(135deg,#8a8a5a,#5e5e38)" role="img" aria-label="Bem casados embrulhados"><span class="plus">+</span><div class="label">BEM CASADO</div></div>
<div class="ph" style="left:321px;top:1468px;width:264px;height:194px;background:linear-gradient(135deg,#b8aea4,#e6dfd6,#9a9088)" role="img" aria-label="Bem casados com renda"></div>
<div class="ph" style="left:611px;top:1468px;width:265px;height:194px;background:linear-gradient(180deg,#3a2a20,#8a6a70)" role="img" aria-label="Mesa com bem casados"></div>
<div class="ph" style="left:901px;top:1468px;width:265px;height:194px;background:linear-gradient(180deg,#6a5a3a,#8a8276,#e4e4e4)" role="img" aria-label="Arranjo floral sobre bem casados"></div>

<h2 class="sec-title" style="top:1718px">MACARONS</h2>
<p class="sec-text" style="top:1762px">Delicados doces crocantes por fora e macios por dentro, que seguem receita francesa, elaborados com<br>farinha de amêndoas.</p>
<p class="sec-text" style="top:1829px">Além de deliciosos, dão um toque colorido às mesas e se destacam em qualquer evento!</p>
<p class="sec-text" style="top:1873px">A nossa linha inclui os seguintes sabores: Pistache, frutas do bosque, limão siciliano, maracujá, côco, chocolate,<br>baunilha, zabaione, caramelo com flor de sal, além da linha floral, composta por rosas, violeta e flor de laranjeira.</p>
<p class="sec-text" style="top:1940px">Experimente e surpreenda-se!</p>
<div class="arrows" style="top:1951px"><span><svg width="14" height="20"><path d="M11 2 3 10l8 8" fill="none" stroke="#5a4f47" stroke-width="2.5"/></svg></span><span><svg width="14" height="20"><path d="M3 2l8 8-8 8" fill="none" stroke="#5a4f47" stroke-width="2.5"/></svg></span></div>

<div class="ph" style="left:34px;top:2010px;width:265px;height:194px;background:linear-gradient(135deg,#6a9ab0,#c8b89a)" role="img" aria-label="Macaron pérola salmão azul"><span class="plus">+</span><div class="label">MACARON PÉROLA SALMÃO</div></div>
<div class="ph" style="left:321px;top:2010px;width:264px;height:194px;background:linear-gradient(135deg,#e8a898,#d8c4a8)" role="img" aria-label="Macarons rosados com pérola"></div>
<div class="ph" style="left:611px;top:2010px;width:265px;height:194px;background:linear-gradient(135deg,#8a7a80,#b0a0a8)" role="img" aria-label="Macarons de violeta"></div>
<div class="ph" style="left:901px;top:2010px;width:265px;height:194px;background:linear-gradient(135deg,#d86080,#e8d040,#60a060)" role="img" aria-label="Taça com macarons coloridos"></div>

<div class="abs footer-line"></div>
<div class="abs footer" role="img" aria-label="Fundo com mesa de doces esmaecida"></div>

<div class="fcol" style="left:48px">
  <svg width="64" height="60" style="margin-left:72px" viewBox="0 0 64 60"><path d="M4 20c0-10 56-10 56 0v6H46v-6c-8-3-20-3-28 0v6H4z" fill="#c5e9ec"/><path d="M16 30h32l6 26H10z" fill="#c5e9ec"/><circle cx="32" cy="42" r="7" fill="#6f776b"/></svg>
  <h3>Atendimento</h3>
  <p style="margin-left:3px">Fone: (11) 95555-0187<br>contato@vebrinola.com.br</p>
</div>
<div class="fcol" style="left:356px">
  <svg width="50" height="66" style="margin-left:72px" viewBox="0 0 50 66"><path d="M25 2C12 2 3 11 3 24c0 16 22 40 22 40s22-24 22-40C47 11 38 2 25 2z" fill="#c5e9ec"/><circle cx="25" cy="23" r="8" fill="#6f776b"/></svg>
  <h3>Onde Estamos</h3>
  <p style="margin-left:3px;font-size:24px;line-height:26px">São Paulo</p>
</div>
<div class="fcol" style="left:668px">
  <svg width="70" height="66" style="margin-left:42px" viewBox="0 0 70 66"><path d="M6 4l10-4 50 54-4 10-10-4z" fill="#c5e9ec"/></svg>
  <h3>Orçamento</h3>
  <p style="font-size:16px;line-height:20px;margin-left:2px">Solicite um orçamento<br>sem compromisso.</p>
  <span class="fbtn" style="margin-top:10px">SOLICITAR</span>
</div>
<div class="fcol" style="left:921px">
  <svg width="76" height="56" style="margin-left:56px;margin-top:4px" viewBox="0 0 76 56"><rect x="2" y="2" width="72" height="52" rx="4" fill="#c5e9ec"/><path d="M8 8l30 24 30-24M8 48l22-18M68 48 46 30" stroke="#6f776b" stroke-width="5" fill="none"/></svg>
  <h3 style="margin-top:6px">Newslatter</h3>
  <p style="font-size:17px;line-height:20px;margin-left:2px">Receba nossas novidades</p>
  <div style="display:flex;align-items:center;gap:6px;margin-top:4px"><svg width="18" height="16"><rect x="1" y="4" width="16" height="11" fill="#fff"/><path d="M1 4l8 6 8-6" stroke="#6f776b" fill="none"/></svg><span style="width:166px;height:22px;background:#fff;display:block"></span></div>
  <span class="fbtn" style="margin:6px 0 0 95px">CADASTRAR</span>
</div>

</body>
</html>
```